Poster design for a company operating care homes in the UK showcasing our core values

We need a poster to display in our care homes showcasing our new core values:

Purpose
We are driven by a clear understanding of why we do what we do: to enrich lives, honour legacies and make a meaningful difference every day, for our residents, their families, our colleagues and our community.

Excellence
We hold ourselves to the highest standards, delivering exceptional care and creating an environment where both residents and staff can thrive.

Openness
We build trust through honest, respectful communication, welcoming feedback, sharing ideas, and embracing change as a path to continuous growth.

Passion
We are passionate about delivering exceptional care. We take pride in what we do and in making a real difference in people’s lives.

Learning
We are committed to personal and professional growth; empowering each other through ongoing development, reflection, and shared knowledge.

Empathy
We actively listen and seek to understand before being understood, recognising the unique stories, feelings, and needs of others.

I have attached a small graphic that we would like you try to incorporate, in addition to our company logo. Please theme the rest of the poster around our company colours.

```html
<!DOCTYPE html>
<html lang="en">
<head>
<meta charset="utf-8">
<title>Alderway – Our Values</title>
<link href="https://fonts.googleapis.com/css2?family=Bebas+Neue&display=swap" rel="stylesheet">
<style>
  :root {
    --navy: #3a5571;
    --hex-navy: #42536d;
    --peach: #efaa88;
    --heading: #3f5069;
    --body: #262833;
    --bg-light: #f4f8fc;
    --bg-dark: #a6c1d6;
  }
  * { margin: 0; padding: 0; box-sizing: border-box; }
  html, body { width: 848px; height: 1200px; overflow: hidden; }
  body {
    position: relative;
    font-family: "Bebas Neue", "Arial Narrow", sans-serif;
    background: radial-gradient(ellipse 900px 900px at 560px 150px, var(--bg-light) 0%, #dde9f3 45%, var(--bg-dark) 100%);
  }
  .brand {
    position: absolute;
    left: 520px;
    top: 186px;
    display: flex;
    align-items: center;
    gap: 12px;
    color: var(--navy);
    font-size: 58px;
    line-height: 1;
    letter-spacing: 2px;
  }
  .brand-mark {
    width: 30px;
    height: 30px;
    background: var(--peach);
  }
  .divider {
    position: absolute;
    left: 180px;
    width: 568px;
    height: 1px;
    background: var(--peach);
  }
  .values-graphic {
    position: absolute;
    left: 100px;
    top: 376px;
    width: 190px;
    height: 696px;
    background: linear-gradient(180deg, var(--peach) 0%, #b59a92 50%, var(--hex-navy) 100%);
    opacity: 0.9;
  }
  .value {
    position: absolute;
    left: 318px;
    width: 430px;
  }
  .value-title {
    color: var(--heading);
    font-size: 24px;
    line-height: 1;
    font-weight: 400;
    letter-spacing: 0.2px;
    margin-bottom: 6px;
  }
  .value-text {
    color: var(--body);
    font-size: 15.5px;
    line-height: 19px;
    letter-spacing: 0.1px;
  }
</style>
</head>
<body>
  <div class="brand"><span class="brand-mark"></span>Alderway</div>

  <div class="divider" style="top:374px"></div>
  <div class="divider" style="top:491px"></div>
  <div class="divider" style="top:606px"></div>
  <div class="divider" style="top:713px"></div>
  <div class="divider" style="top:835px"></div>
  <div class="divider" style="top:935px"></div>
  <div class="divider" style="top:1061px"></div>

  <div class="values-graphic" role="img" aria-label="Decorative column graphic spelling the word People, one letter per value, in peach and navy"></div>

  <section class="value" style="top:390px">
    <h2 class="value-title">Purpose</h2>
    <p class="value-text">We are driven by a clear understanding of why we do what we do:<br>to enrich lives, honour legacies and make a meaningful difference every day,<br>for our residents, their families, our colleagues and our community.</p>
  </section>
  <section class="value" style="top:516px">
    <h2 class="value-title">Excellence</h2>
    <p class="value-text">We hold ourselves to the highest standards, delivering exceptional care and<br>creating an environment where both residents and staff can thrive.</p>
  </section>
  <section class="value" style="top:631px">
    <h2 class="value-title">Openness</h2>
    <p class="value-text">We build trust through honest, respectful communication, welcoming feedback,<br>sharing ideas, and embracing change as a path to continuous growth.</p>
  </section>
  <section class="value" style="top:740px">
    <h2 class="value-title">Passion</h2>
    <p class="value-text">We are passionate about delivering exceptional care. We take pride in what<br>we do and in making a real difference in people’s lives.</p>
  </section>
  <section class="value" style="top:857px">
    <h2 class="value-title">Learning</h2>
    <p class="value-text">We are committed to personal and professional growth; empowering each other<br>through ongoing development, reflection, and shared knowledge.</p>
  </section>
  <section class="value" style="top:957px">
    <h2 class="value-title">Empathy</h2>
    <p class="value-text">We actively listen and seek to understand before being understood,<br>recognising the unique stories, feelings, and needs of others.</p>
  </section>
</body>
</html>
```